Electrical Contractor Brochure, Folder and Letter Head

Barrowfield Electrical Ltd. is an Edmonton based electrical contractor focusing on commercial and industrial electrical services. Our target market is manufacturing facilities, warehouses and commercial buildings.

We want to seem larger than we are with service vehicles and electricians ready to dispatch to service calls and new installations. Our key color is the blue in the logo. The BFE logo is well branded in Edmonton and should be on the brochure.

We are looking for a tri-fold brochure, full-page brochure with folder sleeves and a letter head.
Updates

Please ignore the second page of copy.  I only want the electrical content in the brochure.  This is my mistake.  Please use only the first page of copy.

Industry/Entity Type

Electrical

Requirements
Must have
• Many background pics of the services, electricians and projects. I like the faded BFE logo in the background of the letterhead! Folder Size A4
Nice to have
• Try the pic named Cover Pic1 to on the front of the brochure.
Should not have
• DO NOT USE ANY WEBSITE CONTENT. THIS IS NOT OUR BUSINESS. PLEASE USE ONLY CONTENT AND COLOR FROM THE ATTACHED FILES!!

```html
<!DOCTYPE html>
<html lang="en">
<head>
<meta charset="utf-8">
<title>Barrowfield Electrical Ltd. – Letterhead</title>
<link rel="stylesheet" href="https://fonts.googleapis.com/css2?family=Source+Sans+3:wght@400;700&display=swap">
<style>
  :root {
    --brand-blue: #1560ab;
    --band-dark: #2f2f2f;
    --paper: #ffffff;
    --backdrop: #e9e9e9;
    --footer-text: #ffffff;
  }
  * { margin: 0; padding: 0; box-sizing: border-box; }
  html, body {
    width: 1011px;
    height: 1200px;
    overflow: hidden;
    background: var(--backdrop);
    font-family: "Source Sans 3", "Myriad Pro", Arial, sans-serif;
  }
  .letterhead {
    position: absolute;
    left: 57px;
    top: 20px;
    width: 897px;
    height: 1160px;
    background: var(--paper);
    box-shadow: 0 2px 10px rgba(0,0,0,0.15);
  }
  .brand {
    position: absolute;
    top: 48px;
    left: 0;
    right: 0;
    text-align: center;
    color: var(--brand-blue);
    font-weight: 700;
  }
  .brand-initials {
    display: block;
    font-size: 104px;
    line-height: 1;
    letter-spacing: 4px;
  }
  .brand-name {
    display: block;
    margin-top: 6px;
    font-size: 21px;
    letter-spacing: 2px;
    text-transform: uppercase;
  }
  .letter-body {
    position: absolute;
    top: 190px;
    left: 60px;
    right: 60px;
    bottom: 100px;
  }
  .footer {
    position: absolute;
    left: 0;
    right: 0;
    bottom: 0;
    color: var(--footer-text);
  }
  .footer-address {
    height: 34px;
    background: var(--band-dark);
    display: flex;
    align-items: center;
    justify-content: center;
    font-size: 15px;
    letter-spacing: 1.3px;
  }
  .footer-contact {
    height: 52px;
    background: var(--brand-blue);
    display: flex;
    align-items: center;
    justify-content: center;
    gap: 12px;
    font-size: 15px;
  }
  .contact-item {
    display: inline-flex;
    align-items: center;
    gap: 4px;
  }
  .contact-item svg {
    width: 11px;
    height: 11px;
    fill: none;
    stroke: var(--footer-text);
    stroke-width: 2;
  }
  .contact-item svg .solid { fill: var(--footer-text); stroke: none; }
</style>
</head>
<body>
  <main class="letterhead">
    <header class="brand">
      <span class="brand-initials">BFE</span>
      <span class="brand-name">Barrowfield Electrical Ltd.</span>
    </header>

    <section class="letter-body" aria-label="Letter content"></section>

    <footer class="footer">
      <div class="footer-address">00, complex name, City, state</div>
      <div class="footer-contact">
        <span class="contact-item">
          <svg viewBox="0 0 24 24" aria-hidden="true"><path d="M5 3h4l2 5-3 2a12 12 0 0 0 6 6l2-3 5 2v4a2 2 0 0 1-2 2A18 18 0 0 1 3 5a2 2 0 0 1 2-2z"/></svg>
          123-456-0789
        </span>
        <span class="contact-item">
          <svg viewBox="0 0 24 24" aria-hidden="true"><rect class="solid" x="6" y="2" width="12" height="20" rx="2"/></svg>
          123-456-0789
        </span>
        <span class="contact-item">
          <svg viewBox="0 0 24 24" aria-hidden="true"><rect x="3" y="6" width="18" height="13" rx="1"/><path d="M3 7l9 7 9-7"/></svg>
          info@bfemail.ca
        </span>
        <span class="contact-item">
          <svg viewBox="0 0 24 24" aria-hidden="true"><circle cx="12" cy="12" r="9"/><path d="M3 12h18M12 3c3 3 3 15 0 18M12 3c-3 3-3 15 0 18"/></svg>
          www.bfe.com
        </span>
      </div>
    </footer>
  </main>
</body>
</html>
```